Company letter head and business card for new Indian Pharmaceutical Export company.

We need a letterhead and business card design for an Indian Pharmaceutical Export company.

The letter head needs to contain the following information.
Verona Healthline Pvt. Ltd.
Office No 4837 Plot No 52, Kestrel Heights, RT Lane, 400517, Maharashtra, India.
Email: info@verona-healthline.example
Phone: +91-8213460592
CIN: U58213MH2025PTC719264
GSTIN: (This number is still pending, we will add later)

The business card needs to contain:
Address:
Verona Healthline Pvt. Ltd.
Office No 4837 Plot No52, Kestrel Heights, RT Lane, 400517, MH, India.
Email: tobias@verona-healthline.example
Phone: +49-17638421956
Name on card: Tobias Wendlinger
Position: Director

The design for the letter head and business card should be simple but trustworthy.
Please use only Green and blue, same as in the attached logo.

```html
<!DOCTYPE html>
<html lang="en">
<head>
<meta charset="utf-8">
<title>Verona Healthline Letterhead</title>
<link href="https://fonts.googleapis.com/css2?family=Figtree:wght@400;500;600;700&display=swap" rel="stylesheet">
<style>
  :root {
    --brand-blue: #1b75bb;
    --heading-blue: #0f5f9f;
    --brand-green: #8cc63f;
    --ink: #1f1f1f;
    --muted: #6a6a6a;
    --backdrop: #e1e1e1;
    --paper: #ffffff;
  }
  * { margin: 0; padding: 0; box-sizing: border-box; }
  html, body { width: 1200px; height: 1200px; overflow: hidden; }
  body { background: var(--backdrop); font-family: "Figtree", sans-serif; color: var(--ink); }

  .letterhead {
    position: absolute; left: 216px; top: 76px;
    width: 769px; height: 1046px;
    background: var(--paper); overflow: hidden;
  }

  .brand { position: absolute; left: 52px; top: 34px; width: 116px; text-align: center; }
  .brand-dot { width: 90px; height: 90px; margin: 0 auto 12px; border-radius: 50%; border: 8px solid var(--brand-blue); }
  .brand-name { font-size: 13px; font-weight: 700; color: var(--heading-blue); white-space: nowrap; }

  .company { position: absolute; left: 496px; top: 46px; font-size: 11.8px; line-height: 14px; }
  .company-name { font-size: 13px; font-weight: 600; color: var(--heading-blue); margin-bottom: 1px; letter-spacing: .2px; }
  .company-ids { margin-top: 12px; }

  .backdrop-mark {
    position: absolute; left: 122px; top: 272px; width: 514px; height: 514px;
    border-radius: 50%; border: 34px solid #eef4f9;
  }

  .greeting { position: absolute; left: 50px; top: 261px; font-size: 25px; font-weight: 600; color: var(--heading-blue); }

  .letter-body { position: absolute; left: 51px; top: 309px; width: 659px; font-size: 18.4px; line-height: 23.6px; text-align: justify; }
  .letter-body p + p { margin-top: 23.6px; }

  .sign-off { position: absolute; left: 59px; top: 769px; }
  .signer-name { font-size: 11px; color: #555; }
  .signer-role { font-size: 8.6px; color: var(--muted); margin-top: 2px; }
  .signature { position: absolute; left: 51px; top: 800px; width: 171px; height: 76px;
    background: linear-gradient(90deg, #f3f3f3, #e9e9e9); border-radius: 4px; }

  .contact { position: absolute; top: 976px; left: 0; width: 100%; font-size: 22px; }
  .contact-item { position: absolute; display: flex; align-items: center; gap: 7px; white-space: nowrap; }
  .contact-item.phone { left: 161px; }
  .contact-item.mail { left: 385px; }
  .contact-item svg { display: block; }

  .footer-band { position: absolute; left: 0; bottom: 0; width: 769px; height: 20px; }
</style>
</head>
<body>
  <main class="letterhead">
    <div class="backdrop-mark" aria-hidden="true"></div>

    <div class="brand">
      <div class="brand-dot" aria-hidden="true"></div>
      <div class="brand-name">Verona Healthline</div>
    </div>

    <address class="company" style="font-style:normal">
      <div class="company-name">Verona Healthline Pvt. Ltd.</div>
      <div>Office No 4837 Plot No 52,</div>
      <div>Kestrel Heights, RT Lane, 400517,</div>
      <div>Maharashtra, India.</div>
      <div class="company-ids">
        <div>CIN: U58213MH2025PTC719264</div>
        <div>GSTIN: 00000000</div>
      </div>
    </address>

    <h1 class="greeting">Dear Mr. John,</h1>

    <section class="letter-body">
      <p>Lorem ipsum dolor sit amet, consectetuer adipiscing elit, sed diam nonummy nibh euismod tincidunt ut laoreet dolore magna aliquam erat volutpat. Ut wisi enim ad minim veniam, quis nostrud exerci tation ullamcorper suscipit lobortis nisl ut aliquip ex ea commodo consequat. Duis autem vel eum iriure dolor in hendrerit in vulputate velit esse molestie consequat, vel illum dolore eu feugiat nulla facilisis at vero eros et accumsan et iusto odio dignissim qui blandit praesent luptatum zzril delenit augue duis dolore te feugait nulla facilisi.</p>
      <p>Lorem ipsum dolor sit amet, cons ectetuer adipiscing elit, sed diam nonummy nibh euismod tincidunt ut laoreet dolore magna aliquam erat volutpat. Ut wisi Lorem ipsum dolor sit amet, consectetuer adipiscing elit, sed diam nonummy nibh euismod tincidunt ut laoreet dolore magna aliquam erat volutpat. Ut wisi enim ad minim veniam, quis nostrud exerci tation ullamcorper suscipit lobortis nisl ut aliquip ex ea commodo consequat. Duis autem vel eum iriure dolor in hendrerit in vulputate velit esse molestie consequat,Lorem ipsum dolor sit amet, cons ectetuer adipiscing elit, sed diam nonummy nibh euismod tincidunt ut laoreet dolore magna aliquam erat volutpat.</p>
    </section>

    <div class="sign-off">
      <div class="signer-name">John Doe</div>
      <div class="signer-role">Office Maneger</div>
    </div>
    <div class="signature" role="img" aria-label="Handwritten signature of the office manager"></div>

    <div class="contact">
      <div class="contact-item phone">
        <svg width="22" height="22" viewBox="0 0 24 24" aria-hidden="true"><path fill="var(--heading-blue)" d="M6.6 2.2c.6-.3 1.3-.1 1.6.5l2 3.8c.3.6.1 1.3-.4 1.7l-1.7 1.2c1 2.4 2.9 4.4 5.3 5.5l1.3-1.6c.4-.5 1.1-.7 1.7-.4l3.8 2c.6.3.8 1 .5 1.6l-1.3 2.6c-.4.8-1.3 1.2-2.2 1C9.8 18.6 5.1 13.9 3.6 6.6c-.2-.9.2-1.8 1-2.2z"/></svg>
        <span>+91-8213460592</span>
      </div>
      <div class="contact-item mail">
        <svg width="22" height="16" viewBox="0 0 22 16" aria-hidden="true"><rect x="0" y="0" width="22" height="16" fill="var(--heading-blue)"/><path d="M1 1l10 8 10-8M1 15l7-6M21 15l-7-6" stroke="#fff" stroke-width="1.6" fill="none"/></svg>
        <span>info@verona-healthline.example</span>
      </div>
    </div>

    <svg class="footer-band" viewBox="0 0 769 20" preserveAspectRatio="none" aria-hidden="true">
      <polygon points="0,0 393,0 380,20 0,20" fill="var(--brand-blue)"/>
      <polygon points="402,0 769,0 769,20 389,20" fill="var(--brand-green)"/>
    </svg>
  </main>
</body>
</html>
```